Redesign - Trifold Brochure - Adding new and fresh look.

I have attached what we currently have as a brochure but we need it to be redesigned. The information content is accurate but looking for fresh new design/layout. Please see the images attached. In tif and pdf format. If you need a different format to work please specify and will do my best to upload it.

Target Market(s)

Retail giveaways to educate customers.

Requirements
Must have
• New fresh look

```html
<!DOCTYPE html>
<html lang="en">
<head>
<meta charset="utf-8">
<title>CBD Trifold Brochure – Inside Spread</title>
<link href="https://fonts.googleapis.com/css2?family=Open+Sans:wght@400;600;700;800&display=swap" rel="stylesheet">
<style>
  :root{
    --stage:#3b3b3b;
    --navy:#14303a;
    --ink:#1b3440;
    --teal-dark:#15262c;
    --teal-mid:#23414a;
    --orange:#f4a21c;
    --orange-deep:#ec8a12;
    --green:#9ccb2c;
    --green-light:#b6d93a;
    --grey-band:#d9d9d9;
    --white:#ffffff;
  }
  *{box-sizing:border-box;margin:0;padding:0}
  html,body{width:1200px;height:800px;overflow:hidden;background:var(--stage);font-family:"Open Sans",Arial,sans-serif}
  .spread{position:absolute;left:120px;top:29px;width:960px;height:742px;overflow:hidden;box-shadow:0 12px 30px rgba(0,0,0,.45)}
  .spread-bg{position:absolute;inset:0}
  .photo{position:absolute}
  .photo--oil{left:0;top:0;width:320px;height:450px;
    background:linear-gradient(160deg,#b3281c 0%,#d35a2a 18%,#e9a640 38%,#cfae86 60%,#9c7a52 100%)}
  .photo--body{left:320px;top:0;width:640px;height:470px;
    background:
      radial-gradient(ellipse 110px 210px at 115px 230px,rgba(120,220,230,.55),rgba(60,140,160,.15) 70%,transparent 100%),
      radial-gradient(ellipse 220px 170px at 470px 230px,rgba(190,60,40,.55),rgba(120,40,30,.2) 60%,transparent 100%),
      radial-gradient(ellipse 260px 200px at 240px 260px,rgba(130,150,160,.35),transparent 80%),
      linear-gradient(180deg,var(--teal-dark),var(--teal-mid) 60%,var(--teal-dark))}
  .photo--bottle{left:850px;top:232px;width:78px;height:290px;border-radius:20px 20px 10px 10px;
    background:linear-gradient(90deg,#e8e8e8,#ffffff 45%,#dcdcdc);box-shadow:-4px 6px 12px rgba(0,0,0,.3)}
  .callouts{position:absolute;inset:0;pointer-events:none}
  .callout{position:absolute;border-radius:50%;background:var(--orange);border:2px solid #ffd27a;
    display:flex;align-items:center;justify-content:center;text-align:center;
    font-size:7px;font-weight:700;line-height:1.3;color:var(--ink);padding:10px}
  .panel{position:absolute;top:0;height:742px;width:320px}
  .panel--left{left:0}
  .panel--mid{left:320px}
  .panel--right{left:640px}
  .heading-work{position:absolute;left:34px;top:34px;width:260px;color:var(--white);font-weight:700;font-size:21px;line-height:1.2}
  .body-work{position:absolute;left:34px;top:96px;width:255px;color:#e9eef0;font-size:8.6px;line-height:1.45}
  .what-title{position:absolute;left:26px;top:478px;color:var(--white);font-weight:700;font-size:16px;display:flex;align-items:center;gap:8px}
  .what-text{position:absolute;left:26px;top:506px;width:275px;color:var(--ink);font-size:10px;line-height:1.35}
  .what-lead{position:absolute;left:26px;top:596px;color:var(--ink);font-size:10.5px}
  .ticks{list-style:none}
  .ticks li{position:relative;padding-left:22px}
  .ticks li::before{content:"";position:absolute;left:4px;top:.25em;width:5px;height:9px;border:solid var(--white);border-width:0 3px 3px 0;transform:rotate(45deg)}
  .relief-list{position:absolute;left:30px;top:616px;color:var(--ink);font-weight:700;font-size:12.5px;line-height:1.4}
  .benefits-title{position:absolute;left:26px;top:500px;width:285px;color:var(--navy);font-weight:800;font-size:17px;line-height:1.25}
  .tag{position:absolute;background:var(--navy);color:var(--white);font-weight:800;font-size:12px;letter-spacing:.5px;
    writing-mode:vertical-rl;transform:rotate(180deg);padding:8px 4px;text-align:center}
  .tag--high{left:26px;top:610px;height:78px}
  .tag--low{left:22px;top:560px;height:72px}
  .nutrient-list{position:absolute;color:var(--white);font-size:13px;line-height:1.5;font-weight:600}
  .nutrient-list--high{left:58px;top:612px}
  .nutrient-list--low{left:52px;top:558px}
</style>
</head>
<body>
<div class="spread">
  <svg class="spread-bg" width="960" height="742" viewBox="0 0 960 742" aria-hidden="true">
    <rect width="960" height="742" fill="var(--teal-dark)"/>
    <!-- left panel lower bands -->
    <path d="M0 440 Q140 395 320 440 L320 742 L0 742 Z" fill="var(--grey-band)"/>
    <path d="M0 470 Q150 425 320 470 L320 742 L0 742 Z" fill="var(--green)"/>
    <path d="M0 470 Q150 425 320 470" fill="none" stroke="var(--white)" stroke-width="4"/>
    <!-- middle & right lower bands -->
    <path d="M320 470 Q520 500 700 450 Q840 410 960 380 L960 742 L320 742 Z" fill="var(--green-light)"/>
    <path d="M320 482 Q520 515 700 470 Q840 432 960 405 L960 742 L320 742 Z" fill="var(--white)"/>
    <path d="M320 488 Q520 522 700 478 Q840 440 960 412 L960 742 L320 742 Z" fill="var(--orange)"/>
    <rect x="320" y="600" width="640" height="142" fill="var(--orange-deep)" opacity=".35"/>
  </svg>

  <div class="photo photo--oil" role="img" aria-label="Close-up photo of golden oil dripping from a dropper"></div>
  <div class="photo photo--body" role="img" aria-label="Illustration of a glowing human figure beside a brain on a dark network background"></div>

  <svg class="callouts" width="960" height="742" viewBox="0 0 960 742" aria-hidden="true">
    <g stroke="#cfd8dc" stroke-width="1" fill="none" opacity=".8">
      <path d="M455 205 L500 160 L520 160"/>
      <path d="M455 300 L520 300"/>
      <path d="M460 400 L510 430 L525 430"/>
      <path d="M640 330 L680 330"/>
    </g>
  </svg>
  <div class="callout" style="left:520px;top:125px;width:78px;height:78px">Cb2 receptors are predominantly found in the immune system.</div>
  <div class="callout" style="left:520px;top:255px;width:86px;height:86px">Cb1 and Cb2 receptors are found on the surface of cells in your body that effect your endocannabinoid system.</div>
  <div class="callout" style="left:525px;top:390px;width:84px;height:84px">Cb2 receptors are responsible for the regulation of inflamma-tion which in turn reduces pain.</div>
  <div class="callout" style="left:680px;top:282px;width:100px;height:100px">Cb1 receptors are found primarily in the brain controlling memory processing, motor regulation, appetite, pain sensation, mood, and sleep.</div>

  <section class="panel panel--left">
    <h2 class="what-title">
      <svg width="16" height="16" viewBox="0 0 16 16" aria-hidden="true"><circle cx="8" cy="8" r="8" fill="var(--white)"/><path d="M4 8.5 L7 11 L12 5" stroke="var(--green)" stroke-width="2.2" fill="none"/></svg>
      What is CBD?
    </h2>
    <p class="what-text">one of many compounds called phytocan-nabinoids that is found in various plant species. The industrial hemp plant is a plentiful source of CBD. When derived from industrial hemp, CBD with less than 0.03% THC by weight has no psychoactive properties but retains all of its positive bio-</p>
    <p class="what-lead">CBD is commonly used as relief from:</p>
    <ul class="ticks relief-list">
      <li>Pain</li>
      <li>Inflammation</li>
      <li>Anxiety</li>
      <li>Sleep Disorders</li>
      <li>Neurological Disorders</li>
      <li>Opiate Dependence</li>
    </ul>
  </section>

  <section class="panel panel--mid">
    <h2 class="benefits-title">There are many other benefits from using CBD and hemp products. Hemp products are:</h2>
    <div class="tag tag--high">HIGH IN</div>
    <ul class="ticks nutrient-list nutrient-list--high">
      <li>Omega 3 and 6 Fatty Acids</li>
      <li>Vitamins A &amp; E</li>
      <li>Calcium, Iron &amp; Antioxidants</li>
    </ul>
  </section>

  <section class="panel panel--right">
    <h2 class="heading-work">How Does CBD Work In Your Body?</h2>
    <p class="body-work">Your body produces certain natural compounds called cannabinoids that are used to regulate functions for your entire body. Inside your body there is a processing network for cannabinoids called your Endo-cannabinoid System. CBD mimics the natural cannabinoids produced by your body and stimulates certain receptors found on the surface of cells in your body that effect your ECS. These cells are mainly located in the central nervous system and the immune system. This reaction caused by the introduction of CBD helps balance and maintain and restore your body's natural function. Essentially</p>
    <div class="tag tag--low">LOW IN</div>
    <ul class="ticks nutrient-list nutrient-list--low">
      <li>Saturated Fats</li>
      <li>Cholesterol</li>
      <li>Carbohydrates</li>
    </ul>
  </section>

  <div class="photo photo--bottle" role="img" aria-label="Product photo of a white hemp extract oral spray bottle"></div>
</div>
</body>
</html>
```